New graphics package for website

We're currently about to launch a product to insurance agents and we need to upgrade the graphics package for tundlex.io
The current site is http://tundlex.io
We'd like to upgrade the graphics package for this site - very simple. The site needs to have a very modern and elegant feel.
The site content should remain, we may add some. You can use lorem ipsum you need content to fill a space.
We need to add 3 page links - Home, Enroll, Request invitation
We also have an invitation page that needs to be upgraded (shall not be accessible from main site), the current page for that is: http://www.tundlex.io/webinar.php - content on this page cannot change, just needs a graphics over lay.
Final source files shall be AI or PSD and include all fonts and high-res images included.
Target Market(s)
Business to business - insurance agencies across the US are the only users of this site.
Industry/Entity Type
Insurance
Number of Pages Required
2 page
Requirements
Must have
- Multiple forms only in the inner pages:
- Enroll form for the enroll page.
- Invite form for the invite page
- Invite form shall only have name, email, phone, carrier

```html
<!DOCTYPE html>
<html lang="en">
<head>
<meta charset="utf-8">
<title>tundlex.io</title>
<link href="https://fonts.googleapis.com/css2?family=Oswald:wght@400;500;600&family=Open+Sans:ital,wght@0,400;0,600;0,700;1,400&display=swap" rel="stylesheet">
<style>
:root{
  --orange:#f26b1d;
  --orange-dark:#d9540c;
  --ink:#2b2b2b;
  --text:#6f6f6f;
  --muted:#9a9a9a;
  --light:#f3f3f3;
  --line:#e2e2e2;
  --footer:#262626;
  --white:#ffffff;
}
*{box-sizing:border-box;margin:0;padding:0}
html,body{width:1200px;height:2336px;overflow:hidden}
body{font-family:"Open Sans",Arial,sans-serif;color:var(--text);background:var(--white);position:relative}
.heading{font-family:"Oswald","Arial Narrow",sans-serif;text-transform:uppercase}

/* header */
.site-header{position:absolute;top:0;left:0;width:1200px;height:150px;background:var(--white)}
.brand{position:absolute;left:60px;top:42px;display:flex;align-items:center;gap:14px}
.brand-mark{width:40px;height:40px;border-radius:50%;background:var(--orange)}
.brand-name{font-family:"Open Sans",Arial,sans-serif;font-weight:700;font-size:38px;color:var(--orange);letter-spacing:-0.5px}
.contact-strip{position:absolute;right:60px;top:14px;display:flex;align-items:center;gap:12px}
.contact-icon{width:36px;height:36px;border-radius:50%;background:var(--orange);display:flex;align-items:center;justify-content:center}
.contact-lines{font-size:12px;line-height:16px;color:var(--muted)}
.contact-lines strong{color:var(--ink);font-weight:600}
.main-nav{position:absolute;right:60px;top:96px;display:flex;gap:0}
.main-nav a{display:block;padding:0 26px;font-family:"Oswald",sans-serif;font-size:15px;letter-spacing:1px;color:var(--ink);text-decoration:none;line-height:30px;border-top:3px solid transparent}
.main-nav a.active{color:var(--orange);border-top-color:var(--orange)}

/* hero */
.hero{position:absolute;top:150px;left:0;width:1200px;height:610px;background:linear-gradient(180deg,#a9cf7a 0%,#c9d8a0 25%,#d9b79a 50%,#b98a6d 68%,#8fb546 85%,#6e9a2c 100%)}
.hero-title{position:absolute;top:448px;left:0;width:100%;text-align:center;font-size:46px;font-weight:500;color:var(--white);letter-spacing:1px;text-shadow:0 2px 6px rgba(0,0,0,.35)}
.hero-btn{position:absolute;top:534px;left:529px;width:142px;height:42px;background:rgba(40,40,40,.75);border:1px solid rgba(255,255,255,.6);color:var(--white);font-family:"Oswald",sans-serif;font-size:15px;letter-spacing:1px;text-align:center;line-height:40px}

/* features */
.features{position:absolute;top:760px;left:0;width:1200px;height:170px;background:var(--light);border-bottom:1px solid var(--line);display:flex;justify-content:center;gap:40px;padding-top:40px}
.feature{width:300px;display:flex;gap:16px}
.feature-icon{flex:none;width:64px;height:64px;border-radius:50%;border:2px solid var(--orange);display:flex;align-items:center;justify-content:center;background:var(--white)}
.feature-title{font-size:14px;font-weight:700;color:var(--orange);text-transform:uppercase;margin:6px 0 6px}
.feature-text{font-size:11.5px;line-height:17px}

/* markets */
.markets{position:absolute;top:930px;left:0;width:1200px;height:430px}
.markets-copy{position:absolute;left:100px;top:62px;width:560px}
.markets-title{font-size:27px;font-weight:500;color:var(--orange);letter-spacing:.5px}
.markets-sub{font-size:10.5px;color:var(--muted);text-transform:uppercase;margin:12px 0 18px;font-weight:600}
.markets-text{font-size:12.5px;line-height:20px}
.btn-orange{display:inline-block;background:var(--orange);color:var(--white);font-family:"Oswald",sans-serif;font-size:14px;letter-spacing:1px;padding:0 22px;line-height:38px;margin-top:34px}
.markets-photo{position:absolute;left:760px;top:70px;width:340px;height:320px;background:linear-gradient(160deg,#555 0%,#2f2f2f 55%,#1d1d1d 100%);border:6px solid var(--white);box-shadow:0 0 0 1px var(--line)}
.divider{position:absolute;top:1360px;left:100px;width:1000px;height:1px;background:var(--line)}

/* blog */
.blog{position:absolute;top:1400px;left:100px;width:610px}
.section-title{font-size:24px;font-weight:500;color:var(--orange)}
.section-title::after{content:"";display:block;width:50px;height:3px;background:var(--orange);margin-top:8px}
.post{display:flex;gap:22px;margin-top:34px}
.post-photo{flex:none;width:180px;height:130px;border:4px solid var(--white);box-shadow:0 0 0 1px var(--line)}
.post-photo.one{background:linear-gradient(160deg,#e8e4df,#b99a86 60%,#6c5a4d)}
.post-photo.two{background:linear-gradient(160deg,#e9eef0,#d6b399 55%,#a0362f)}
.post-title{font-size:18px;font-weight:500;color:var(--ink);letter-spacing:.3px}
.post-meta{font-size:10px;color:var(--muted);margin:8px 0 10px;display:flex;gap:14px}
.post-meta span::before{content:"";display:inline-block;width:7px;height:7px;border-radius:50%;background:var(--orange);margin-right:5px}
.post-text{font-size:11.5px;line-height:18px}
.post-text b{color:var(--orange);font-weight:700}

/* enroll */
.enroll{position:absolute;top:1400px;left:760px;width:340px}
.enroll-sub{font-size:10.5px;color:var(--muted);text-transform:uppercase;font-weight:600;margin-top:6px}
.enroll-form{margin-top:18px;background:#e9e9e9;padding:22px 26px}
.field{height:36px;background:var(--white);border:1px solid #d7d7d7;margin-bottom:12px;font-size:11px;color:var(--muted);padding:0 12px;line-height:34px;display:flex;justify-content:space-between}
.enroll-btn{width:130px;margin:8px auto 0;background:var(--orange);color:var(--white);text-align:center;font-family:"Oswald",sans-serif;font-size:15px;letter-spacing:1px;line-height:38px}
.enroll-note{text-align:center;font-size:10px;color:var(--muted);margin-top:8px}

/* testimonials */
.testimonials{position:absolute;top:1862px;left:0;width:1200px;height:328px;background:linear-gradient(180deg,var(--orange) 0%,var(--orange-dark) 100%);text-align:center;color:var(--white)}
.testimonials-title{margin-top:40px;font-size:26px;font-weight:400;letter-spacing:1px;display:flex;justify-content:center;align-items:center;gap:20px}
.testimonials-title::before,.testimonials-title::after{content:"";width:70px;height:1px;background:rgba(255,255,255,.6)}
.quote{width:840px;margin:28px auto 0;font-size:13px;line-height:22px;font-style:italic;position:relative}
.quote-mark{font-family:"Oswald",sans-serif;font-size:40px;line-height:0;vertical-align:-14px;font-style:normal;margin:0 4px}
.quote-author{margin-top:14px;font-size:12px;font-style:italic}
.dots{display:flex;justify-content:center;gap:10px;margin-top:24px}
.dots i{width:10px;height:10px;border-radius:50%;background:rgba(255,255,255,.5)}
.dots i.on{background:var(--white)}

/* footer */
.site-footer{position:absolute;top:2190px;left:0;width:1200px;height:146px;background:var(--footer)}
.footer-nav{position:absolute;left:100px;top:52px;display:flex;gap:14px;font-size:12px;color:#cfcfcf;text-transform:uppercase;font-weight:600}
.footer-nav span.sep{color:#666}
.copyright{position:absolute;left:100px;top:84px;font-size:10.5px;color:#7d7d7d}
.social{position:absolute;right:100px;top:46px;display:flex;gap:12px}
.social i{width:36px;height:36px;border-radius:50%;background:var(--orange)}
</style>
</head>
<body>

<header class="site-header">
  <div class="brand"><span class="brand-mark"></span><span class="brand-name">tundlex.io</span></div>
  <div class="contact-strip">
    <span class="contact-icon">
      <svg width="18" height="18" viewBox="0 0 24 24"><path fill="#fff" d="M6.6 10.8a15.1 15.1 0 006.6 6.6l2.2-2.2c.3-.3.7-.4 1-.2 1.1.4 2.3.6 3.6.6.6 0 1 .4 1 1V20c0 .6-.4 1-1 1A17 17 0 013 4c0-.6.4-1 1-1h3.5c.6 0 1 .4 1 1 0 1.3.2 2.5.6 3.6.1.3 0 .7-.2 1z"/></svg>
    </span>
    <div class="contact-lines">hello@tundlex.io<br><strong>Call us: (555) 010-4821</strong></div>
  </div>
  <nav class="main-nav">
    <a class="active">HOME</a><a>ENROLL</a><a>REQUEST INVITATION</a><a>CONTACT US</a>
  </nav>
</header>

<section class="hero" role="img" aria-label="Photo of a smiling family lying together on green grass">
  <h1 class="hero-title heading">Prospects are every where, get in front of them</h1>
  <div class="hero-btn">VIEW MORE</div>
</section>

<section class="features">
  <div class="feature">
    <span class="feature-icon"><svg width="30" height="30" viewBox="0 0 24 24"><path fill="none" stroke="#f26b1d" stroke-width="2" d="M12 2l8 3v6c0 5-3.5 9-8 11-4.5-2-8-6-8-11V5z"/><path fill="none" stroke="#f26b1d" stroke-width="2" d="M8 12l3 3 5-6"/></svg></span>
    <div><div class="feature-title">Simply random text</div><p class="feature-text">Contrary to belief, lorem ipsum is not simply random text, it has roots in a piece of classical literature.</p></div>
  </div>
  <div class="feature">
    <span class="feature-icon"><svg width="30" height="30" viewBox="0 0 24 24"><path fill="none" stroke="#f26b1d" stroke-width="2" d="M3 11l9-7 9 7M6 9v11h12V9"/><rect x="10" y="14" width="4" height="6" fill="#f26b1d"/></svg></span>
    <div><div class="feature-title">Simply random text</div><p class="feature-text">Contrary to belief, lorem ipsum is not simply random text, it has roots in a piece of classical literature.</p></div>
  </div>
  <div class="feature">
    <span class="feature-icon"><svg width="30" height="30" viewBox="0 0 24 24"><path fill="#f26b1d" d="M12 3C6.5 3 2 7 2 12h20c0-5-4.5-9-10-9z"/><path fill="none" stroke="#f26b1d" stroke-width="2" d="M12 12v7a2 2 0 01-4 0"/></svg></span>
    <div><div class="feature-title">Simply random text</div><p class="feature-text">Contrary to belief, lorem ipsum is not simply random text, it has roots in a piece of classical literature.</p></div>
  </div>
</section>

<section class="markets">
  <div class="markets-copy">
    <h2 class="markets-title heading">Dominate your local insurance markets</h2>
    <p class="markets-sub">From the words of agencysite.example</p>
    <p class="markets-text">A new type of insurance marketing product has taken the local agency market by storm, giving agents a simple way to reach nearby prospects. Our tool lets your agency connect with local buyers at the moment they look for cover, building trust and a steady flow of quality leads. Lorem ipsum dolor sit amet, consectetur adipiscing elit, sed do eiusmod tempor incididunt ut labore et dolore magna aliqua, ut enim ad minim veniam, quis nostrud exercitation ullamco laboris nisi ut aliquip ex ea commodo.</p>
    <span class="btn-orange">READ MORE</span>
  </div>
  <div class="markets-photo" role="img" aria-label="Photo of a confident businessman in a suit in front of a chalkboard drawing of strong arms"></div>
</section>

<div class="divider"></div>

<section class="blog">
  <h2 class="section-title heading">Latest blog</h2>
  <article class="post">
    <div class="post-photo one" role="img" aria-label="Photo of a businesswoman at her desk"></div>
    <div>
      <h3 class="post-title heading">Perspiciatis unde omnis iste natus error</h3>
      <div class="post-meta"><span>Published in Insurance</span><span>Posted By Admin</span><span>12 Comments</span></div>
      <p class="post-text">Sed ut perspiciatis unde omnis iste natus error sit voluptatem accusantium doloremque laudantium, totam rem aperiam, eaque ipsa quae ab illo inventore veritatis et quasi architecto beatae vitae dicta sunt. <b>READ MORE</b></p>
    </div>
  </article>
  <article class="post">
    <div class="post-photo two" role="img" aria-label="Photo of a smiling young man in a red shirt"></div>
    <div>
      <h3 class="post-title heading">Perspiciatis unde omnis iste natus error</h3>
      <div class="post-meta"><span>Published in Insurance</span><span>Posted By Admin</span><span>8 Comments</span></div>
      <p class="post-text">Sed ut perspiciatis unde omnis iste natus error sit voluptatem accusantium doloremque laudantium, totam rem aperiam, eaque ipsa quae ab illo inventore veritatis et quasi architecto beatae vitae dicta sunt. <b>READ MORE</b></p>
    </div>
  </article>
</section>

<aside class="enroll">
  <h2 class="section-title heading">Enroll</h2>
  <p class="enroll-sub">For tundlex marketing</p>
  <form class="enroll-form">
    <div class="field">Name</div>
    <div class="field">Email</div>
    <div class="field">Phone</div>
    <div class="field">Select Carrier <span>&#9662;</span></div>
    <div class="field">Select State <span>&#9662;</span></div>
    <div class="enroll-btn">ENROLL</div>
    <p class="enroll-note">All fields are required</p>
  </form>
</aside>

<section class="testimonials">
  <h2 class="testimonials-title heading">Testimonials</h2>
  <p class="quote"><span class="quote-mark">&ldquo;</span>Nemo enim ipsam voluptatem quia voluptas sit aspernatur aut odit aut fugit, sed quia consequuntur magni dolores eos qui ratione voluptatem sequi nesciunt. Neque porro quisquam est, qui dolorem ipsum quia dolor sit amet, consectetur, adipisci velit, sed quia non numquam eius modi tempora incidunt ut labore et dolore magnam aliquam quaerat voluptatem.<span class="quote-mark">&rdquo;</span></p>
  <p class="quote-author">&mdash; omnplatum deleniti</p>
  <div class="dots"><i class="on"></i><i></i><i></i><i></i></div>
</section>

<footer class="site-footer">
  <nav class="footer-nav"><span>Home</span><span class="sep">|</span><span>Enroll</span><span class="sep">|</span><span>Request Invitation</span><span class="sep">|</span><span>Contact Us</span></nav>
  <p class="copyright">&copy; tundlex.io Professional Insurance Marketing. All rights reserved.</p>
  <div class="social"><i></i><i></i><i></i><i></i><i></i></div>
</footer>

</body>
</html>
```